Business card for a "family office" company

Please provide professional looking business card designs, incorporating the attached logo and below details. Harrowmere Holdings Pty Ltd is a family office / financial investment company. We are looking for a modern, professional and contemporary card design.

Industry/Entity Type

Finance

Contact Information for Business Card

Name: Dean Mollick
Title: Director
Company: Harrowmere Holdings Pty Ltd
Email: harrowdean@quillnet.example
Mobile: 0462 735 418
Address: 4/312 Barnaby Parade, Larkfield WA 6140, Australia

Requirements
Must have
• All details above and the logo. logo only on back side. incorporate colours of logo
Nice to have
• up to you
Should not have
• ?

```html
<!DOCTYPE html>
<html lang="en">
<head>
<meta charset="utf-8">
<title>Harrowmere Holdings – Business Card</title>
<link rel="stylesheet" href="https://fonts.googleapis.com/css2?family=Cormorant+SC:wght@500;600&family=Cormorant+Garamond:wght@500&display=swap">
<style>
  :root {
    --navy: #1f2160;
    --paper: #ffffff;
    --stage: #ffffff;
    --shadow: rgba(0, 0, 0, 0.28);
  }
  * { margin: 0; padding: 0; box-sizing: border-box; }
  html, body {
    width: 972px; height: 1200px; overflow: hidden;
    background: var(--stage);
  }
  .sheet { position: relative; width: 972px; height: 1200px; }
  .card {
    position: absolute;
    width: 676px; height: 404px;
    background: var(--paper);
    box-shadow: 10px 14px 22px var(--shadow);
    overflow: hidden;
  }
  .card-front { left: 146px; top: 144px; }
  .card-back  { left: 152px; top: 692px; }

  /* Front: name mark */
  .brand {
    position: absolute; left: 0; right: 0; top: 106px;
    text-align: center; color: var(--navy);
    font-family: "Cormorant SC", serif; font-weight: 600;
  }
  .brand-square {
    display: block; width: 84px; height: 84px; margin: 0 auto 22px;
    background: var(--navy);
  }
  .brand-name { display: block; font-size: 52px; line-height: 1; letter-spacing: 1px; }
  .brand-sub  { display: block; font-size: 18px; letter-spacing: 9px; margin-top: 8px; }

  /* Back */
  .holder {
    position: absolute; left: 0; right: 0; top: 40px;
    text-align: center; color: var(--navy);
    font-family: "Cormorant SC", serif; font-weight: 500;
  }
  .holder-title { font-size: 31px; letter-spacing: 3px; line-height: 1.2; }
  .holder-company { font-size: 20px; letter-spacing: 2.5px; margin-top: 4px; }

  .contact {
    position: absolute; left: 192px; top: 176px;
    list-style: none; color: var(--navy);
    font-family: "Cormorant Garamond", serif; font-weight: 500;
    font-size: 17px; line-height: 26px;
  }
  .contact li { display: flex; align-items: flex-start; margin-bottom: 12px; }
  .contact svg { width: 20px; height: 20px; margin: 3px 26px 0 0; flex: none; fill: var(--navy); }
  .band {
    position: absolute; left: 0; right: 0; bottom: 0; height: 22px;
    background: var(--navy);
  }
</style>
</head>
<body>
<main class="sheet">
  <section class="card card-front" aria-label="Card front">
    <div class="brand">
      <span class="brand-square"></span>
      <span class="brand-name">Harrowmere</span>
      <span class="brand-sub">Holdings</span>
    </div>
  </section>

  <section class="card card-back" aria-label="Card back">
    <div class="holder">
      <p class="holder-title">Director Dean Mollick</p>
      <p class="holder-company">Harrowmere Holdings Pty Ltd</p>
    </div>
    <ul class="contact">
      <li>
        <svg viewBox="0 0 20 20" aria-hidden="true"><rect x="1" y="5" width="18" height="11" rx="1"/></svg>
        <span>harrowdean@quillnet.example</span>
      </li>
      <li>
        <svg viewBox="0 0 20 20" aria-hidden="true"><path d="M5 2l3 4-2 2c1 2.5 3.5 5 6 6l2-2 4 3-2 3C9 18 2 11 2 4z"/></svg>
        <span>0462 735 418</span>
      </li>
      <li>
        <svg viewBox="0 0 20 20" aria-hidden="true"><path d="M10 1a6 6 0 0 0-6 6c0 4.5 6 12 6 12s6-7.5 6-12a6 6 0 0 0-6-6zm0 8.5a2.5 2.5 0 1 1 0-5 2.5 2.5 0 0 1 0 5z"/></svg>
        <span>4/312 Barnaby Parade,<br>Larkfield WA 6140, Australia</span>
      </li>
    </ul>
    <div class="band"></div>
  </section>
</main>
</body>
</html>
```